Brochure Design - ICT Company

We are an ICT (Information & Communication Technologies) company and need a brochure design. Our main products and services are Office Equipment, Banking Equipment, Software Solutions, IT Hardware, Networking & Communication, Audio Video Solutions and Social Media Marketing. Please check our website www.dalvorinex.com for details in our Solutions menu.

Designs should include colors from our website (blue) and our logo (orange/green) in the best possible combination with lighter colors. Graphics and patterns should be sleek and modern. Brochure size to be square shaped (21 cm x 21 cm).

Final design should portray us as a futuristic technology company.

Provide a design with sample images and we can purchase them if required. Alternatively, let us know if the images from our website will suffice.
Updates

Project Deadline Extended
Reason: Awaiting more designs and more creativity. If any input is required from us, do inform asap.

Uploaded 2 sample brochure designs that we found interesting - looking for more inspiring ideas.

Thanks

Hi everyone, the following text should appear on the cover of the brochure design:

'Your One Stop Solution Provider for Information & Communication Technologies'

Project Deadline Extended
Reason: Awaiting management feedback - might require changes in design. Open to receiving more designs.

Thank you all for participating. Received many creative ideas and will be back with more requests. 

Target Market(s)

Decision Makers in UAE: IT Managers, Purchase Manager, CEO, Finance Managers etc

Industry/Entity Type

Communication

Requirements
Must have
• We have 7 divisions within our company. Brochure should dedicate 2 pages to each company - Text on one side and Image on the other.

7 divisions are: (details on website)
Office Equipment - sales of copiers, fax etc to any industry, any size office
Banking Equipment - sales of coin counters, counterfeit detectors etc to banks and foreign exchange houses
IT & Communication - providing server, email, software licenses to any industry, any size office
Software Solution - Quillon partner + provide software solution to any industry, any size company
ELV & Security - provide CCTV, security systems to big companies, warehouses etc any industry
AV & Convergence - provide latest technology multi sensory solutions for theatres, opera houses, education sector, hospitality sector, medical sector etc.
Social Media Marketing - provide marketing options to companies through social media (www.dalvoripost.com)

Images to be used in the brochure are attached - they are concept images associated with each division. The design for the inner pages can be created around this basic image.

Cover page - design with logo, 'An Information & Technologies Company'
Back page - Design with address details
Inner sections:
1. About Us
2. Seven divisions as described above

The pattern for the text for inner pages should be:
Heading describing problem
Small Paragraph text describing solution
Small inset images of the

Nice to have
• Modern, sleek look with images that reflect an ICT/IT company - stand out from the regular brochure design
Should not have
• The design should not use old-style design, fonts etc.

```html
<!DOCTYPE html>
<html lang="en">
<head>
<meta charset="utf-8">
<title>Dalvorin Technologies – Office Systems</title>
<link href="https://fonts.googleapis.com/css2?family=Archivo+Black&family=Arimo:wght@400;700&family=Varela+Round&display=swap" rel="stylesheet">
<style>
  :root {
    --paper: #ffffff;
    --ink: #1f1f1f;
    --sky-panel: #a9d9e8;
    --brand-blue: #1b6db4;
    --lime-panel: #bfd62f;
    --accent-orange: #e9731c;
    --pill-yellow: #f6e21b;
    --pill-blue: #2aa6de;
    --pill-orange: #f7941d;
    --pill-green: #8dc63f;
    --pill-teal: #1db4a4;
    --dash: #c9c9c9;
    --sphere-light: #f2f2f2;
    --sphere-dark: #8e8e8e;
  }
  * { margin: 0; padding: 0; box-sizing: border-box; }
  html, body { width: 1200px; height: 600px; overflow: hidden; background: var(--paper); }
  .spread {
    position: relative; width: 1200px; height: 600px; overflow: hidden;
    background: var(--paper); font-family: "Arimo", Arial, sans-serif; color: var(--ink);
  }
  .guides { position: absolute; inset: 0; }

  .about-panel {
    position: absolute; left: 0; top: 115px; width: 286px; height: 485px;
    background: var(--sky-panel); padding: 18px 16px 0 26px;
  }
  .about-title {
    font-family: "Archivo Black", "Arial Black", sans-serif; font-weight: 400;
    font-size: 45px; letter-spacing: -2.2px; word-spacing: -4px;
    color: var(--brand-blue); line-height: 1; margin-left: 3px; white-space: nowrap;
  }
  .about-copy {
    margin-top: 9px; font-size: 9.8px; line-height: 11.4px; color: #2b2b2b;
  }

  .paper-sphere {
    position: absolute; left: 313px; top: 38px; width: 525px; height: 525px; border-radius: 50%;
    background: radial-gradient(circle at 42% 35%, var(--sphere-light) 0%, #d4d4d4 55%, var(--sphere-dark) 100%);
  }
  .pill {
    position: absolute; display: flex; align-items: center; justify-content: center;
    text-align: center; font-family: "Varela Round", Arial, sans-serif; color: #1a1a1a;
    border-radius: 34px; line-height: 1.02; font-size: 24px;
  }
  .pill--copier { left: 497px; top: 103px; width: 140px; height: 68px; background: var(--pill-yellow); }
  .pill--fax { left: 614px; top: 204px; width: 168px; height: 62px; background: var(--pill-blue); }
  .pill--standard { left: 340px; top: 240px; width: 236px; height: 42px; background: var(--pill-orange); }
  .pill--toner { left: 553px; top: 305px; width: 230px; height: 62px; background: var(--pill-green); }
  .pill--admin { left: 397px; top: 385px; width: 184px; height: 88px; background: var(--pill-teal); }

  .brand-name {
    position: absolute; left: 1068px; top: 34px; width: 110px;
    font-size: 9px; font-weight: 700; line-height: 11px; color: #3a3a3a;
  }

  .product-label { position: absolute; font-weight: 700; color: var(--ink); white-space: nowrap; }
  .product-label--copy { left: 878px; top: 80px; font-size: 13.5px; }
  .product-label--print { left: 962px; top: 118px; font-size: 13.5px; }
  .product-label--large { left: 1001px; top: 159px; font-size: 11px; }
  .product-label--fax { left: 1015px; top: 211px; font-size: 11px; }
  .product-label--shred { left: 1002px; top: 250px; font-size: 11px; }
  .product-label--baling { left: 964px; top: 294px; font-size: 11px; }

  .office-title {
    position: absolute; left: 940px; top: 376px; white-space: nowrap;
    font-family: "Archivo Black", "Arial Black", sans-serif; font-weight: 400;
    font-size: 24px; letter-spacing: -1px; word-spacing: -3px; color: var(--accent-orange);
  }
  .office-panel { position: absolute; left: 852px; top: 418px; width: 348px; height: 182px; background: var(--lime-panel); }
  .office-copy {
    position: absolute; left: 862px; top: 428px; width: 312px;
    font-size: 8.6px; font-weight: 700; line-height: 10.4px; color: #1e1e1e;
  }
</style>
</head>
<body>
<main class="spread">
  <svg class="guides" width="1200" height="600" viewBox="0 0 1200 600" aria-hidden="true">
    <g fill="none" stroke="var(--dash)" stroke-width="1.5" stroke-dasharray="8 6">
      <line x1="0" y1="101" x2="380" y2="101"/>
      <line x1="268" y1="0" x2="268" y2="101"/>
      <line x1="382" y1="0" x2="382" y2="101"/>
      <circle cx="575" cy="300" r="276"/>
      <line x1="845" y1="410" x2="1200" y2="410"/>
      <polyline points="845,410 845,568 1178,568 1178,410"/>
    </g>
    <g fill="none" stroke="#8a8a8a" stroke-width="2" stroke-dasharray="9 6">
      <line x1="828" y1="213" x2="872" y2="96"/>
      <line x1="828" y1="213" x2="955" y2="133"/>
      <line x1="828" y1="213" x2="994" y2="169"/>
      <line x1="828" y1="213" x2="1008" y2="218"/>
      <line x1="828" y1="213" x2="995" y2="257"/>
      <line x1="828" y1="213" x2="956" y2="298"/>
    </g>
  </svg>

  <section class="about-panel">
    <h1 class="about-title">About Us</h1>
    <p class="about-copy">Every business faces security challenges. It doesn't matter if you are the neighborhood grocery store, or the biggest bank in the world, you need security measures in place. Some companies may need security cameras to monitor things or access control systems to restrict access to certain areas. Other companies may need rising arm barriers, road blocks, or even tire killers to prevent traffic from going into high security areas. Every business needs a good smoke alarm and fire alarm system to ensure everyone's safety, and most all companies these days have some form of public address/speaker system and security alarm systems. What if there was a company your business was able to count on for all of these security needs?<br>
    There is a company you can count on, and it is Dalvorin Technologies! We provide all of the services described above, and many, many more! Our goal is to make your company safe and secure! Whatever security challenges you may be facing, we are here to help! We have had over 15 years of experience in this industry, and our customers are always our number one priority! We are experts in the business security field and we can apply the highest technologies available to help your business! You can trust that when you choose us for your security needs, you are dealing with a top notch company whose goal is to serve you well, and make your company the best that it can be!<br>
    If you think Dalvorin Technologies would be a good fit to help your company with any security needs, feel free to reach out to us! We are always ready to help, and look forward to hearing from you! Just call us for a demo or visit our website at: http://www.dalvorinex.com/ for more information!</p>
  </section>

  <div class="paper-sphere" role="img" aria-label="Sphere built from crumpled invoices and urgent paper documents"></div>
  <div class="pill pill--copier">Copier<br>contracts</div>
  <div class="pill pill--fax">Fax service<br>agreements</div>
  <div class="pill pill--standard">No standardization</div>
  <div class="pill pill--toner">Toner from<br>multiple suppliers</div>
  <div class="pill pill--admin">High<br>administration<br>costs</div>

  <p class="brand-name">DALVORIN TECHNOLOGIES L.L.C.</p>

  <span class="product-label product-label--copy">Copy Systems</span>
  <span class="product-label product-label--print">Print Systems</span>
  <span class="product-label product-label--large">Large Format Systems</span>
  <span class="product-label product-label--fax">FAX Machines</span>
  <span class="product-label product-label--shred">Schredding Machines</span>
  <span class="product-label product-label--baling">Baling Machines</span>

  <h2 class="office-title">Office Systems</h2>
  <div class="office-panel"></div>
  <p class="office-copy">We are the prime distributors of office automation systems, based out from Dubai. Our custom made solution improves efficiency of your daily business process. Being able to do your daily schedules with minimized errors and more effectively means that you can lift your bottom line... Do more with less time and effort. This means significant cost savings and more time to focus on core business functions. Our award-winning range of color and monochrome products offers cost-effective, high-performance, high-value document management solutions for any office environment. Our multi-functional product range delivers a broad range of print/copy/scan/fax speeds up your business process to the maximum performance.</p>
</main>
</body>
</html>
```